School Fairs flyer design

We are running school fairs (Northfield Residential Academies Expo in East Africa) in February 2018. The school fairs and information sessions will take place in Rwanda (February 6th-8th, Kenya February 9th-10th and Uganda on February 11th-12th.)

Rwanda:
Kigali School Fair: February 7th, 1:30-5:30PM
Student Interviews: February 8th, 9:00-1PM
Location: Kigali Lumora Hotel

For information:
Phone number: +250736482915
Email: info@tovaradvisors.example
www.tovarlearningadvisors.example

Features:
*6 US Boarding Schools representative
*Learn about the application process and apply in person.
* Bring your transcripts/school reports to Interview
* www.tovarlearningadvisors.example

Target Market(s)

Students age 11-20 and their parents

Industry/Entity Type

Education

Contact Information for Business Card

Marcel Habarugira
Executive Director
Tovar Consultants
Dallas, Texas
Marcel@tovaradvisers.example
www.tovaradvisors.example
+1614-527-3186

Number of Pages Required

4 page

Font styles to use
Serif

Colors

Designer to choose colors to be used in the design.

Requirements
Must have
• Very clean, elegant and professional designs. Since we offer educational services to students and families, school tours and fairs, as well as institutional support. We would like the designs to reflect what we do.
Nice to have
• Global view, a new logo that incorporates things from our existing logo. We will use this more often but the targeted population is the same.
Should not have
• off colors

```html
<!DOCTYPE html>
<html lang="en">
<head>
<meta charset="utf-8">
<title>Northfield Residential Academies Expo – Flyer</title>
<link href="https://fonts.googleapis.com/css2?family=Varela+Round&display=swap" rel="stylesheet">
<style>
  :root {
    --page-bg: #ececec;
    --flyer-mint: #c6e8d8;
    --ink-navy: #10283d;
    --ribbon-coral: #f46f6f;
    --ribbon-text: #ffffff;
    --dates-green: #3e6d5e;
    --road-dark: #3a3d42;
    --brand-blue: #1d3f8a;
    --brand-green: #7cb342;
    --flag-neutral: #8aa89b;
  }
  * { margin: 0; padding: 0; box-sizing: border-box; }
  html, body {
    width: 1125px; height: 1200px; overflow: hidden;
    background: var(--page-bg);
    font-family: "Varela Round", "Helvetica Neue", Arial, sans-serif;
  }
  .flyer {
    position: absolute; left: 169px; top: 41px;
    width: 787px; height: 1118px;
    background: var(--flyer-mint);
    overflow: hidden;
  }
  .bunting {
    position: absolute; left: 0; top: 0; width: 787px; height: 182px;
    background: linear-gradient(180deg, rgba(244,111,111,0.0) 0%, rgba(240,170,90,0.35) 40%, rgba(150,200,120,0.3) 70%, rgba(198,232,216,0) 100%);
  }
  .brand {
    position: absolute; top: 198px; left: 0; width: 100%;
    display: flex; justify-content: center; align-items: center; gap: 12px;
  }
  .brand-dot {
    width: 22px; height: 22px; border-radius: 50%; background: var(--brand-green);
  }
  .brand-name {
    font-size: 28px; color: var(--brand-blue); letter-spacing: 0.5px;
  }
  .event-title {
    position: absolute; top: 270px; left: 0; width: 100%;
    text-align: center; color: var(--ink-navy);
    font-size: 62px; line-height: 82px; font-weight: 400;
  }
  .date-ribbon {
    position: absolute; left: 78px; top: 473px; width: 631px; height: 81px;
  }
  .date-ribbon svg { position: absolute; inset: 0; }
  .date-ribbon-text {
    position: absolute; inset: 0; display: flex; align-items: center; justify-content: center;
    color: var(--ribbon-text); font-size: 34px;
  }
  .country-dates {
    position: absolute; top: 570px; left: 0; width: 100%;
    list-style: none; text-align: center; color: var(--dates-green);
    font-size: 28px; line-height: 37px;
  }
  .flag-chip {
    display: inline-block; width: 26px; height: 16px; margin-right: 6px;
    background: var(--flag-neutral); vertical-align: 1px;
  }
  .school-scene {
    position: absolute; left: 10px; top: 830px; width: 767px; height: 247px;
    background: linear-gradient(180deg, rgba(198,232,216,0) 0%, #e3b655 35%, #d9824a 60%, #6f9a4a 100%);
    border-radius: 6px 6px 0 0;
  }
  .road {
    position: absolute; left: 0; top: 1077px; width: 100%; height: 41px;
    background: var(--road-dark);
  }
</style>
</head>
<body>
  <main class="flyer">
    <div class="bunting" role="img" aria-label="Colourful party bunting flags strung across the top"></div>

    <div class="brand">
      <span class="brand-dot"></span>
      <span class="brand-name">Tovar Consultants</span>
    </div>

    <h1 class="event-title">Northfield Residential<br>Academies Expo</h1>

    <div class="date-ribbon">
      <svg viewBox="0 0 631 81" width="631" height="81" aria-hidden="true">
        <polygon points="0,4 631,0 614,40 631,81 14,81 28,42" fill="var(--ribbon-coral)"/>
      </svg>
      <div class="date-ribbon-text">February 2018 6th Feb - 12th Feb</div>
    </div>

    <ul class="country-dates">
      <li><span class="flag-chip"></span>Rwanda February 6th-8th</li>
      <li><span class="flag-chip"></span>Kenya February 9th-10th</li>
      <li><span class="flag-chip"></span>Uganda on February 11th-12th.</li>
    </ul>

    <div class="school-scene" role="img" aria-label="Illustrated school building with clock tower, trees and a yellow school bus"></div>
    <div class="road"></div>
  </main>
</body>
</html>
```